Sol Bocado Digital Menu Boards

IF SELECTED, WINNER MAY BE HIRED FOR OTHER DESIGNS OF DIFFERENT STORES OF OUR COMPANY.

Task: Digital Menu Boards Design

Task description: We need designs for a Digital Menu to be displayed on two 42’’screens at Solbocado, a fast-food restaurant in Guadalajara, Mexico. The menu redesign should communicate to our customers the experience of eating at our restaurant.

For avoiding the creation of videos, we are expecting several menu slides with the same text but with different images, simulating the effect of a video where the images are changing. This menu slides will be projected through a USB memory and a slideshow.

Attached files:
For the design, there are several documents attached to the task description:
1. Logo of the restaurant
2. Pictures of the restaurant
3. Example video of what we want to achieve through this menu slides.
4. Pictures of the actual menu board, to be replaced with the new designs.
5. Menu description (regular and breakfast menu)
6. Pictures of each element on the menu (We don’t have yet any breakfast pictures)
**The files are organized on a ZIP file.

Expected product:
For the regular menu,
• 2 menu slide designs for TACOS Y ESPECIALIDADES, where the text will be exactly the same but the images would differ.
• 2 menu slide designs for BEBIDAS Y EXTRAS, where the text will be exactly the same but the images would differ.
For the breakfast menu,
• 1 menu slide including all the menu
Total: 5 menu board slides.

Technical specs:
• You should send the editable file, med and high resolution JPGs for each design.
• The designs should fit perfectly on 42’’ screens.

Reason: Designers, For the final decision we are asking for a minimum of designs for chosing, we are going to wait a little bit more. Solbocado

Industry/Entity Type

Restaurant

```html
<!DOCTYPE html>
<html lang="es">
<head>
<meta charset="utf-8">
<title>Sol Bocado – Desayunos</title>
<link href="https://fonts.googleapis.com/css2?family=Bebas+Neue&display=swap" rel="stylesheet">
<style>
  :root {
    --stage: #f4f4f4;
    --cream: #fdf3df;
    --ink: #1e1e1e;
    --bar: #2a2a2a;
    --white: #ffffff;
    --rule: #6a6a6a;
    --food-warm: #c98c5a;
    --food-light: #efe1c6;
    --food-red: #a8432b;
    --sun: #f1dba8;
  }
  * { margin: 0; padding: 0; box-sizing: border-box; }
  html, body { width: 1200px; height: 799px; overflow: hidden; background: var(--stage); }
  body { position: relative; font-family: 'Bebas Neue', 'Arial Narrow', sans-serif; color: var(--ink); }

  .menu-board {
    position: absolute; left: 0; top: 62px;
    width: 1200px; height: 675px;
    background: var(--cream);
    overflow: hidden;
  }
  .footer-band {
    position: absolute; left: 0; bottom: 0;
    width: 100%; height: 79px;
    background: var(--ink);
  }

  .dish-photo { position: absolute; left: 25px; top: 28px; width: 371px; height: 247px; }

  .label-bar {
    position: absolute;
    background: var(--bar);
    color: var(--white);
    display: flex; align-items: center; justify-content: center;
    letter-spacing: 1px;
    outline: 2px dotted var(--white);
    outline-offset: -6px;
  }
  .dish-label { left: 54px; top: 303px; width: 342px; height: 54px; font-size: 34px; }
  .section-title { left: 565px; top: 138px; width: 515px; height: 76px; font-size: 48px; }

  .brand {
    position: absolute; left: 40px; top: 470px;
    display: flex; align-items: center; gap: 18px;
  }
  .brand-mark { width: 76px; height: 76px; border-radius: 50%; background: var(--sun); }
  .brand-name { font-size: 62px; color: var(--ink); line-height: 1; }

  .price-table {
    position: absolute; left: 503px; top: 240px;
    width: 634px;
    border-collapse: collapse;
  }
  .price-table th {
    font-weight: 400; font-size: 19px; text-align: center;
    height: 32px; vertical-align: bottom; padding-bottom: 6px;
  }
  .price-table td {
    font-size: 23px; text-align: center;
    height: 39px; vertical-align: bottom; padding-bottom: 4px;
    border-bottom: 2px dotted var(--rule);
  }
  .price-table .item { text-align: left; width: 160px; }
  .price-table .col-a { width: 140px; }
  .price-table .col-b { width: 120px; }
</style>
</head>
<body>
  <main class="menu-board">
    <svg class="dish-photo" viewBox="0 0 371 247" role="img" aria-label="Photo of quesadillas with meat, melted cheese, guacamole and pico de gallo">
      <defs>
        <linearGradient id="dishTones" x1="0" y1="0" x2="1" y2="1">
          <stop offset="0" stop-color="var(--food-light)"/>
          <stop offset="0.5" stop-color="var(--food-warm)"/>
          <stop offset="1" stop-color="var(--food-red)"/>
        </linearGradient>
      </defs>
      <path d="M20 40 Q30 14 70 16 L220 8 Q280 2 320 30 Q362 60 358 140 Q356 215 300 232 L90 240 Q30 240 22 190 Q10 110 20 40 Z"
            fill="url(#dishTones)" stroke="var(--ink)" stroke-width="2" stroke-dasharray="2 5"/>
    </svg>

    <div class="label-bar dish-label">Quesadillas</div>

    <div class="brand">
      <span class="brand-mark"></span>
      <span class="brand-name">Sol Bocado</span>
    </div>

    <h1 class="label-bar section-title">Desayunos</h1>

    <table class="price-table">
      <thead>
        <tr><th class="item"></th><th class="col-a">Chilaquiles</th><th class="col-b">Burritos</th><th>Tacos Dorados (3)</th></tr>
      </thead>
      <tbody>
        <tr><td class="item">Pastor</td><td>$40</td><td>$45</td><td>$40</td></tr>
        <tr><td class="item">Arrachera</td><td>$50</td><td>$45</td><td>$45</td></tr>
        <tr><td class="item">Queso</td><td></td><td>$45</td><td></td></tr>
        <tr><td class="item">Huevo</td><td></td><td>$45</td><td></td></tr>
      </tbody>
    </table>

    <div class="footer-band"></div>
  </main>
</body>
</html>
```